Women's Online Clothing Boutique Needs Business Cards

I already have a logo that I would like to use. Some of the things that interest me is black business cards, foil embossed logo, glossy embossed logo, leopard print, no yellow font, rounded edges. I even like just a large logo on the front side with all of my information on the back side.

Contact Information for Business Card

https://silverheron.shopvenlo.com/
https://www.pagelink.net/thesilverheronboutique/
https://www.picfeed.net/thesilverheronboutique/
silverheronboutique@mailora.net

Requirements
Must have
• My Logo
Nice to have
• Leopard Print
Should not have
• No Yellow Font

```html
<!DOCTYPE html>
<html lang="en">
<head>
<meta charset="utf-8">
<title>The Silver Heron Boutique – Business Cards</title>
<link href="https://fonts.googleapis.com/css2?family=Lato:wght@400&display=swap" rel="stylesheet">
<style>
  :root {
    --backdrop: #2e2926;
    --card: #17171b;
    --edge: #c9981f;
    --gold: #c9981f;
    --emboss: #4a4a50;
    --contact: #c9c9cc;
  }
  html, body {
    margin: 0;
    padding: 0;
    width: 1200px;
    height: 847px;
    overflow: hidden;
    background: var(--backdrop);
  }
  .canvas {
    position: relative;
    width: 1200px;
    height: 847px;
    display: flex;
    align-items: center;
    justify-content: center;
    gap: 40px;
  }
  .card {
    position: relative;
    width: 540px;
    height: 310px;
    background: var(--card);
    border: 3px solid var(--edge);
    border-radius: 10px;
    box-sizing: border-box;
    box-shadow: 0 12px 30px rgba(0,0,0,0.45);
    overflow: hidden;
  }
  .brand-name {
    margin: 0;
    font-family: "Lato", sans-serif;
    font-weight: 400;
    text-align: center;
  }
  /* Front */
  .card--front .brand-name {
    position: absolute;
    left: 40px; right: 40px; top: 96px;
    font-size: 44px;
    line-height: 56px;
    color: var(--emboss);
  }
  /* Back */
  .card--back .brand-name {
    position: absolute;
    right: 44px; top: 38px;
    width: 260px;
    font-size: 26px;
    line-height: 32px;
    color: var(--gold);
  }
  .icon-row {
    position: absolute;
    right: 54px; top: 140px;
    width: 240px;
    display: flex;
    align-items: center;
    justify-content: center;
    gap: 6px;
  }
  .icon-row .line { flex: 1; height: 1px; background: var(--gold); }
  .icon-row svg { display: block; }
  .contact-list {
    position: absolute;
    right: 40px; top: 180px;
    margin: 0; padding: 0;
    list-style: none;
    text-align: right;
    font-family: "Lato", sans-serif;
    font-weight: 400;
    font-size: 16px;
    line-height: 23px;
    color: var(--contact);
  }
</style>
</head>
<body>
<main class="canvas">
  <section class="card card--front" aria-label="Card front">
    <p class="brand-name">The Silver Heron<br>Boutique</p>
  </section>

  <section class="card card--back" aria-label="Card back">
    <p class="brand-name">The Silver Heron<br>Boutique</p>
    <div class="icon-row">
      <span class="line"></span>
      <svg width="20" height="20" viewBox="0 0 20 20" aria-label="Email">
        <circle cx="10" cy="10" r="9.5" fill="var(--gold)"/>
        <rect x="5" y="6.5" width="10" height="7" fill="none" stroke="var(--card)" stroke-width="1.2"/>
        <path d="M5 6.5 L10 10.5 L15 6.5" fill="none" stroke="var(--card)" stroke-width="1.2"/>
      </svg>
      <svg width="20" height="20" viewBox="0 0 20 20" aria-label="Website">
        <circle cx="10" cy="10" r="9.5" fill="var(--gold)"/>
        <circle cx="10" cy="10" r="5" fill="none" stroke="var(--card)" stroke-width="1.2"/>
        <ellipse cx="10" cy="10" rx="2.2" ry="5" fill="none" stroke="var(--card)" stroke-width="1"/>
        <line x1="5" y1="10" x2="15" y2="10" stroke="var(--card)" stroke-width="1"/>
      </svg>
      <svg width="20" height="20" viewBox="0 0 20 20" aria-label="Page link">
        <circle cx="10" cy="10" r="9.5" fill="var(--gold)"/>
        <rect x="4.5" y="8" width="6" height="4" rx="2" fill="none" stroke="var(--card)" stroke-width="1.2"/>
        <rect x="9.5" y="8" width="6" height="4" rx="2" fill="none" stroke="var(--card)" stroke-width="1.2"/>
      </svg>
      <svg width="20" height="20" viewBox="0 0 20 20" aria-label="Photo feed">
        <circle cx="10" cy="10" r="9.5" fill="var(--gold)"/>
        <rect x="5" y="6" width="10" height="8" fill="none" stroke="var(--card)" stroke-width="1.2"/>
        <path d="M6 13 L9 9.5 L11 11.5 L12.5 10 L14 13 Z" fill="var(--card)"/>
      </svg>
      <span class="line"></span>
    </div>
    <ul class="contact-list">
      <li>silverheronboutique@mailora.net</li>
      <li>silverheron.shopvenlo.com</li>
      <li>www.pagelink.net/thesilverheronboutique/</li>
      <li>www.picfeed.net/thesilverheronboutique/</li>
    </ul>
  </section>
</main>
</body>
</html>
```